Stationery for Public Accountant Practice

Name of Practice
Holloway Merrick Pty Ltd
Tel: 0413927056
Postal Address : PO Box 482, Oakvale East, Vic 3187

Target Market(s)

Small Business Clients

Industry/Entity Type

Accounting

Font styles to use
Serif

Requirements
Must have
• Letterhead, business card, With compliments slip
Nice to have
• Conservative

```html
<!DOCTYPE html>
<html lang="en">
<head>
<meta charset="utf-8">
<title>Holloway Merrick Stationery</title>
<link rel="stylesheet" href="https://fonts.googleapis.com/css2?family=Cinzel:wght@400&family=Open+Sans:wght@400&display=swap">
<style>
  :root {
    --charcoal: #3b3b3d;
    --gold: #c0904e;
    --paper: #ffffff;
    --ink: #4a4a4a;
    --rule: #b5b5b5;
    --silver: #cfcfcf;
    --stage: #ffffff;
  }
  * { box-sizing: border-box; margin: 0; padding: 0; }
  html, body { width: 1200px; height: 1155px; overflow: hidden; background: var(--stage); }
  body { position: relative; font-family: "Open Sans", Arial, sans-serif; color: var(--ink); }

  .sheet { position: absolute; box-shadow: 3px 5px 10px rgba(0,0,0,.28); }
  .brand { font-family: "Cinzel", Georgia, serif; color: var(--charcoal); letter-spacing: .02em; display: flex; align-items: center; white-space: nowrap; }
  .brand-dot { border: 1.5px solid var(--gold); border-radius: 50%; flex: none; }

  /* Letterhead */
  .letterhead { left: 77px; top: 79px; width: 485px; height: 682px; background: var(--paper); border: 1px solid #e4e4e4; }
  .letterhead .brand { position: absolute; left: 50px; top: 34px; font-size: 16px; gap: 9px; }
  .letterhead .brand-dot { width: 34px; height: 34px; }
  .letterhead .sender { position: absolute; right: 33px; top: 44px; text-align: right; font-size: 7.5px; line-height: 10px; font-style: normal; }
  .letterhead .rule { position: absolute; left: 65px; right: 30px; top: 107px; height: 1px; background: var(--rule); }
  .letterhead .letter { position: absolute; left: 66px; top: 144px; width: 349px; font-size: 7.6px; line-height: 16.4px; }
  .letter .recipient { margin-bottom: 16px; }
  .letter p { text-align: justify; }
  .letter .sign { margin-top: 16px; }
  .band { position: absolute; left: 0; right: 0; bottom: 0; background: var(--charcoal); }
  .letterhead .band { height: 13px; }

  /* Presentation folder */
  .folder { left: 650px; top: 79px; width: 484px; height: 682px; background: var(--charcoal); display: flex; flex-direction: column; align-items: center; justify-content: center; gap: 16px; }
  .folder-ring { width: 130px; height: 130px; border: 3px solid var(--gold); border-radius: 50%; }
  .folder-name { font-family: "Cinzel", Georgia, serif; color: var(--gold); font-size: 17px; letter-spacing: .04em; }

  /* Business cards */
  .card { top: 867px; width: 255px; height: 148px; }
  .card-front { left: 48px; background: var(--paper); border: 1px solid #e4e4e4; }
  .card-front .brand { position: absolute; left: 12px; top: 11px; font-size: 11px; gap: 6px; }
  .card-front .brand-dot { width: 25px; height: 25px; }
  .card-front .holder { position: absolute; right: 17px; top: 66px; text-align: right; }
  .holder-name { font-size: 8.5px; letter-spacing: .08em; color: var(--charcoal); }
  .holder-role { font-size: 5.5px; color: #777; }
  .card-front .contacts { position: absolute; left: 13px; top: 104px; font-size: 7px; line-height: 12px; }
  .contacts div { display: flex; align-items: center; gap: 5px; }
  .contacts svg { width: 6px; height: 7px; }
  .card-front .postal { position: absolute; right: 17px; top: 104px; text-align: right; font-size: 7px; line-height: 12px; }
  .card-front .band { height: 13px; }
  .card-back { left: 336px; background: var(--charcoal); }
  .card-back .brand { position: absolute; left: 0; right: 0; top: 32px; flex-direction: column; gap: 5px; color: #bdbdbd; font-size: 11px; }
  .card-back .brand-dot { width: 25px; height: 25px; }
  .card-back .web { position: absolute; left: 0; right: 0; bottom: 11px; text-align: center; font-size: 6px; color: #a9a9a9; }

  /* With compliments slip */
  .comp-slip { left: 634px; top: 823px; width: 536px; height: 245px; background: var(--paper); border: 1px solid #e4e4e4; }
  .comp-slip .top-band { position: absolute; left: 0; top: 0; width: 100%; height: 50px; background: var(--charcoal); }
  .comp-slip .brand { position: absolute; left: 29px; top: 66px; font-size: 11.5px; gap: 7px; }
  .comp-slip .brand-dot { width: 26px; height: 26px; }
  .comp-slip .greeting { position: absolute; left: 30px; top: 124px; font-family: "Cinzel", Georgia, serif; font-size: 18px; color: var(--gold); letter-spacing: .04em; }
  .comp-slip .mark { position: absolute; left: 369px; top: 80px; width: 112px; height: 112px; border: 3px solid var(--silver); border-radius: 50%; }
  .comp-slip .postal { position: absolute; left: 30px; top: 202px; font-size: 7px; line-height: 10px; font-style: normal; }
</style>
</head>
<body>

<section class="sheet letterhead">
  <div class="brand"><span class="brand-dot"></span>Holloway Merrick</div>
  <address class="sender">PO Box 482<br>Oakvale East, Vic 3187<br>0413927056</address>
  <div class="rule"></div>
  <div class="letter">
    <div class="recipient">Trenz Pruca<br>Title<br>Company Name<br>4321 First Street<br>Anytown, State ZIP<br>Date 1/30/12</div>
    <p>Dear Trenz,</p>
    <p>Lorem ipsum dolor sit amet, consectetur adipiscing elit, set eiusmod tempor incidunt et labore et dolore magna aliquam. Ut enim ad minim veniam, quis nostrud exerc. Irure dolor in reprehend incididunt ut labore et dolore magna aliqua. Ut enim ad minim veniam, quis nostrud exercitation ullam mmodo consequet. Duis aute in voluptate velit esse cillum dolore eu fugiat nulla pariatur.</p>
    <p>At vver eos et accusam dignissum qui blandit est praesent. Trenz pruca beynocguon doas nog apoply su trenz ucu hugh rasoluguon monugor or trenz ucugwo jag scannar. We have lassed trenzsa gwo producgs su idfoBraid, yop quiel geg ba solaly rasponsubla rof trenzur sala ent dusgrubuguon. Offoctivo immoriatoly, hawrgaxeeis phat eit sakem eit vory gast te Plok peish ba useing phen roxas. Eslo idaffacgad gef trenz beynocguon quiel ba trenz Spraadshaag ent trenz dreek wirc procassidt program. Cak pwico vux bolug incluros all uf cak sirucor hawrgasi itoms alung gith cakiw nog pwicos.</p>
    <p>Plloaso mako nuto uf cakso dodtos anr koop a cupy uf cak vux noaw yerw phuno. Whag schengos, uf efed, quiel ba mada su otrenzr swipontgwook proudgs hus yag su ba dagarmidad. Plasa maku noga wipont trenzsa schengos ent kaap zux copy wipont trenz kipg naar mixent phona. Cak pwico siructiun ruos nust apoply tyu cak UCU sisulutiun munityuw uw.</p>
    <p>Sincerely yours,</p>
    <p class="sign">Name Here</p>
  </div>
  <div class="band"></div>
</section>

<section class="sheet folder">
  <div class="folder-ring"></div>
  <div class="folder-name">Holloway Merrick</div>
</section>

<section class="sheet card card-front">
  <div class="brand"><span class="brand-dot"></span>Holloway Merrick</div>
  <div class="holder">
    <div class="holder-name">R. ASHCOMBE</div>
    <div class="holder-role">Chief Financial Officer</div>
  </div>
  <div class="contacts">
    <div><svg viewBox="0 0 6 8" aria-hidden="true"><rect x="0.6" y="0.5" width="4.8" height="7" rx="0.8" fill="none" stroke="#c0904e" stroke-width="0.9"/></svg>0413927056</div>
    <div><svg viewBox="0 0 6 8" aria-hidden="true"><circle cx="3" cy="3" r="2.6" fill="#c0904e"/><path d="M1 4.5 L3 7.8 L5 4.5Z" fill="#c0904e"/></svg>www.hollowaymerrick.com</div>
  </div>
  <div class="postal">PO Box 482<br>Oakvale East, Vic 3187</div>
  <div class="band"></div>
</section>

<section class="sheet card card-back">
  <div class="brand"><span class="brand-dot"></span>Holloway Merrick</div>
  <div class="web">www.hollowaymerrick.com</div>
</section>

<section class="sheet comp-slip">
  <div class="top-band"></div>
  <div class="brand"><span class="brand-dot"></span>Holloway Merrick</div>
  <div class="greeting">With Compliments</div>
  <div class="mark"></div>
  <address class="postal">PO Box 482<br>Oakvale East, Vic 3187</address>
</section>

</body>
</html>
```